Professional Services/Construction Management (Millwork) Biz Cards

We've decided on a logo and have our color palette set, now we want to design some very professional looking cards that make a strong first impression - they'll reflect our tagline (that we're going to put on the back: Innovative. Professional. Leaders.

The example business card shows generally the direction we've been thinking of going for the back side - **but we're open to other ideas**

Target Market(s)

The cards should target more high-end (wealthy) owners and general contracting companies. We want them to convey a strong first impression - in a professional and not garish way.

Industry/Entity Type

Construction Company

Contact Information for Business Card

There needs to be a place for our company contractor's license number and business address. We want to also have people's names, titles, phone number, email address. The back can be the logo, tagline and web address

Requirements
Must have
• follow our color palette
Nice to have
• Font & Styles should compliment the Harbor Joinery fonts, but not necessarily match exactly

```html
<!DOCTYPE html>
<html lang="en">
<head>
<meta charset="utf-8">
<title>Harbor Joinery – Business Cards</title>
<link rel="stylesheet" href="https://fonts.googleapis.com/css2?family=Saira:wght@400;500;600;700&family=Open+Sans:ital,wght@1,400;1,600&display=swap">
<style>
  :root {
    --page-bg: #e4e4e4;
    --card-white: #ffffff;
    --bark: #5e4e41;
    --mauve: #a3857f;
    --leaf: #5a9e3f;
    --ink: #5a4f47;
    --cream: #f4efec;
  }
  * { margin: 0; padding: 0; box-sizing: border-box; }
  html, body {
    width: 1105px; height: 1200px; overflow: hidden;
    background: var(--page-bg);
  }
  .sheet { position: relative; width: 1105px; height: 1200px; }
  .card {
    position: absolute; left: 196px; width: 720px; height: 411px;
    border-radius: 19px; overflow: hidden;
  }
  .card--front { top: 146px; background: var(--card-white); }
  .card--back { top: 602px; background: var(--bark); }

  .contact {
    position: absolute; left: 65px; top: 52px;
    font-family: "Saira", sans-serif; color: var(--ink);
  }
  .contact__name { font-size: 26px; font-weight: 600; color: var(--bark); letter-spacing: 0.5px; line-height: 1.2; }
  .contact__title { font-size: 18px; color: var(--leaf); line-height: 1.3; }
  .contact__license { margin-top: 46px; font-size: 19px; line-height: 1.3; }
  .contact__address { margin-top: 10px; font-size: 19px; line-height: 1.35; }
  .contact__lines { margin-top: 14px; list-style: none; }
  .contact__lines li { display: flex; align-items: center; gap: 12px; font-size: 18px; line-height: 30px; }
  .contact__lines svg { width: 17px; height: 17px; fill: var(--bark); flex: none; }

  .brand-front {
    position: absolute; left: 360px; top: 0; width: 320px; height: 411px;
    display: flex; flex-direction: column; align-items: center; justify-content: center; gap: 26px;
  }
  .brand-front__dot { width: 170px; height: 170px; border-radius: 50%; background: var(--mauve); }
  .brand-front__name {
    font-family: "Saira", sans-serif; font-weight: 700; font-size: 34px;
    color: var(--leaf); letter-spacing: 1px; text-transform: uppercase;
  }

  .brand-back {
    position: absolute; left: 0; top: 70px; width: 100%;
    display: flex; flex-direction: column; align-items: center;
  }
  .brand-back__dot { width: 130px; height: 130px; border-radius: 50%; background: var(--mauve); }
  .brand-back__name {
    margin-top: 20px; font-family: "Saira", sans-serif; font-weight: 700; font-size: 30px;
    color: var(--cream); letter-spacing: 1px; text-transform: uppercase;
  }
  .tagline {
    margin-top: 14px; font-family: "Open Sans", sans-serif; font-style: italic; font-weight: 600;
    font-size: 20px; color: var(--card-white);
  }
  .web {
    margin-top: 2px; font-family: "Open Sans", sans-serif; font-style: italic;
    font-size: 17px; letter-spacing: 1.5px; color: var(--cream);
  }
</style>
</head>
<body>
<main class="sheet">
  <section class="card card--front">
    <div class="contact">
      <p class="contact__name">DANIEL REYES</p>
      <p class="contact__title">CEO/Founder</p>
      <p class="contact__license">lic no 41207583</p>
      <p class="contact__address">214 Cedar Wharf Road<br>Juneau, Alaska 99801</p>
      <ul class="contact__lines">
        <li><svg viewBox="0 0 24 24" aria-hidden="true"><path d="M6.6 10.8a15.1 15.1 0 0 0 6.6 6.6l2.2-2.2c.3-.3.7-.4 1-.2 1.1.4 2.3.6 3.6.6.6 0 1 .4 1 1V20c0 .6-.4 1-1 1A17 17 0 0 1 3 4c0-.6.4-1 1-1h3.5c.6 0 1 .4 1 1 0 1.3.2 2.5.6 3.6.1.3 0 .7-.2 1z"/></svg>907 555 0142</li>
        <li><svg viewBox="0 0 24 24" aria-hidden="true"><path d="M2 5h20v14H2zm2 2v.4l8 5 8-5V7zm0 2.8V17h16V9.8l-8 5z"/></svg>hello@harborjoinery.com</li>
        <li><svg viewBox="0 0 24 24" aria-hidden="true"><path d="M12 2a10 10 0 1 0 0 20 10 10 0 0 0 0-20zm-1 17.9A8 8 0 0 1 4.1 10.6L9 15.5v1a2 2 0 0 0 2 2zm6.9-2.5a2 2 0 0 0-1.9-1.4h-1v-3a1 1 0 0 0-1-1H8v-2h2a1 1 0 0 0 1-1V7h2a2 2 0 0 0 2-2v-.4a8 8 0 0 1 2.9 12.8z"/></svg>www.harborjoinery.com</li>
      </ul>
    </div>
    <div class="brand-front">
      <div class="brand-front__dot"></div>
      <p class="brand-front__name">Harbor Joinery</p>
    </div>
  </section>

  <section class="card card--back">
    <div class="brand-back">
      <div class="brand-back__dot"></div>
      <p class="brand-back__name">Harbor Joinery</p>
      <p class="tagline">Innovative. Professional. Leaders.</p>
      <p class="web">www.harborjoinery.com</p>
    </div>
  </section>
</main>
</body>
</html>
```